Solo consultant in research/analytics/data science space needs new business card

I need a new business card to promote my solo business as creative problem solver and consultant. I work on business projects for sales and market research and analytics, customer/market insights, and data science. I provide clients data-informed insights and ideas to enhance their businesses. My initial tagline: 'Make your data work for YOU.'

People should hire me because of my diverse background. Because of my Ph.D. in Political Science I have a strong background in research and analytics, project design and management, and communications skills. With my experience as a marketing analyst, a volunteer on non-profit projects, and currently as research consultant I have worked on projects within various industries. I also have a taste for improvisation so I enjoy thinking creatively and appreciate design thinking.

As an introduction to my background: Clients might want to hire me for many types of projects. Clients might wish to understand who their best customers are and how to characterize them. Maybe clients want to know how their customers feel about a certain product or service. Clients might want to know more about their local market area and overall industry. Clients might want to know whether their marketing programs are effective or else what drives their sales revenue. Perhaps clients want to use their data to create something useful for themselves or their customers.

One client hired me to help them decide whether to expand their services to newer customers. I gathered and analyzed information about the local area – the characteristics of people living there as well as the client’s competitors – and described trends and implications. The client was very pleased with the results and submitted them to superiors for approval to move forward.

For another client – who was looking to purchase a house in a metropolitan area – I gathered population and school data about the area. With this, I created an interactive mapping tool so they could zoom in on neighborhoods and learn more about them before they selected a neighborhood to purchase a house. They were happy with the results of my work.

When I worked as a marketing analyst for a consulting firm, a Vice President of Marketing hired us to discover whether or not the company’s marketing programs (i.e. coupons and discounts) were effective. I analyzed their data and our team discovered their marketing was indeed effective. He was very happy and used this to justify their programs to the Finance department (who thought such programs lost revenue).

- Marcus Delano Whitby, Ph.D.

Target Market(s)

Future clients and employers. The most immediate target markets will be other service providers such as consulting companies, marketing firms and ad agencies. I will also use this for meeting with clients in various industries.

Industry/Entity Type

Consulting

Contact Information for Business Card

Since it is my first real business card as a solo practitioner, I want to make an excellent first impression. I want this useful in case someone hires me to work on projects or else hire me to work within a firm or company. The card should convey competence and some creativity while also being neither stuffy nor a data geek.

Colors

Designer to choose colors to be used in the design.

Requirements
Nice to have
• Attached are the starting efforts at the card to add some color. It will be nice to use my name and descriptors on one side and tagline on the other. If anyone has better ideas, I will love to see them!

```html
<!DOCTYPE html>
<html lang="en">
<head>
<meta charset="UTF-8">
<title>Marcus Delano Whitby, Ph.D. — Business Card</title>
<link href="https://fonts.googleapis.com/css2?family=Bebas+Neue&family=Oswald:wght@600&family=Roboto:wght@400;700&display=swap" rel="stylesheet">
<style>
  :root {
    --stage: #2b2d30;
    --paper: #ffffff;
    --ink: #1e1e1e;
    --ink-soft: #3a3a3a;
    --band: #e4e4e4;
    --name-band: #bdbdbd;
    --rule: #8a8a8a;
    --accent: #b3262a;
    --back: #060606;
    --back-ink: #ffffff;
  }
  * { box-sizing: border-box; margin: 0; padding: 0; }
  html, body { width: 1200px; height: 900px; overflow: hidden; }
  body {
    background: var(--stage);
    display: flex;
    align-items: center;
    justify-content: center;
    gap: 48px;
  }
  .card {
    width: 525px;
    height: 300px;
    position: relative;
    overflow: hidden;
  }

  /* Front */
  .card--front { background: var(--paper); color: var(--ink); }
  .front__name {
    position: absolute;
    left: 34px; top: 32px;
    font-family: 'Oswald', sans-serif;
    font-weight: 600;
    font-size: 26px;
    letter-spacing: 1px;
    line-height: 1.3;
    padding: 0 10px;
    background: var(--name-band);
    color: var(--ink);
    white-space: nowrap;
  }
  .front__name .surname { text-transform: uppercase; }
  .front__specialties {
    position: absolute;
    left: 0; right: 0; top: 96px;
    height: 34px;
    background: var(--band);
    border-top: 1.5px solid var(--rule);
    border-bottom: 1.5px solid var(--rule);
    font-family: 'Roboto', sans-serif;
    font-size: 15.5px;
    color: var(--ink-soft);
    display: flex;
    align-items: center;
    padding-left: 40px;
    padding-top: 2px;
    white-space: nowrap;
  }
  .front__identity {
    position: absolute;
    left: 40px; top: 160px;
    font-family: 'Roboto', sans-serif;
    font-size: 13px;
    line-height: 1.35;
    color: var(--ink-soft);
  }
  .front__identity .role { font-weight: 700; color: var(--ink); font-size: 14px; }
  .front__identity .handle { display: flex; align-items: center; gap: 6px; }
  .front__identity .dot {
    width: 9px; height: 9px; border-radius: 50%;
    background: var(--accent);
  }
  .front__divider {
    position: absolute;
    left: 255px; top: 175px;
    width: 1.5px; height: 78px;
    background: var(--ink-soft);
  }
  .front__contact {
    position: absolute;
    right: 40px; top: 210px;
    font-family: 'Roboto', sans-serif;
    font-style: normal;
    font-size: 15px;
    line-height: 1.3;
    color: var(--ink);
    text-align: right;
  }

  /* Back */
  .card--back { background: var(--back); color: var(--back-ink); }
  .back__tagline {
    position: absolute;
    left: 48px; top: 38px;
    border: 2px solid var(--back-ink);
    padding: 14px 22px 10px 16px;
    font-family: 'Bebas Neue', sans-serif;
    font-size: 40px;
    line-height: 0.95;
    letter-spacing: 2px;
  }
  .back__brand {
    position: absolute;
    right: 44px; bottom: 36px;
    font-family: 'Bebas Neue', sans-serif;
    font-size: 26px;
    line-height: 1;
    letter-spacing: 1.5px;
    color: var(--back-ink);
  }
</style>
</head>
<body>
  <section class="card card--front" aria-label="Business card front">
    <h1 class="front__name"><span class="surname">Marcus Delano Whitby</span>, Ph.D.</h1>
    <p class="front__specialties">Research/Analytics - Customer Intelligence - Data Science</p>
    <div class="front__identity">
      <p class="role">Consultant</p>
      <p class="location">Lisbon, PT</p>
      <p class="handle"><span class="dot"></span>@MarcusWhitby70</p>
    </div>
    <div class="front__divider"></div>
    <address class="front__contact">
      <p>+351 912 305 648</p>
      <p>MDWhitby70@mailbox.com</p>
      <p>MarcusDelanoWhitby.com</p>
    </address>
  </section>

  <section class="card card--back" aria-label="Business card back">
    <p class="back__tagline">Make your<br>data work<br>for you</p>
    <p class="back__brand">Whitby Analytics</p>
  </section>
</body>
</html>
```